Design eines Praxisschilds für Hausarztpraxis
Zielgruppe
Hausarztpraxis, Zielgruppe sind die Bewohner vor Ort, bodenständig
Aufgabenstellung
Praxisschild entwerfen, es soll schlicht sein. Das angefügte Logo bitte verwenden, ggf. auch nur das Symbol ohne Namen verwenden und den Namen extra in schwarz aufführen.
Farben:
- schwarz
- Pantone 13-0645 Limeade
- Pantone 7726
Text:
Dr. med. Jonas Walbrecht
Facharzt für Innere Medizin
Facharzt für Allgemeinmedizin
Sprechzeiten:
Montag bis Freitag 07:30 – 12:00 Uhr
Dienstag und Donnerstag 17:00 – 19:00 Uhr
und nach Vereinbarung
Tel: 0761 83172
www.hausarzt-beispielau.de
Format quer (die Maße sind leider vorgegeben): 55,7 cm x 42,8 cm

```html
<!DOCTYPE html>
<html lang="de">
<head>
<meta charset="utf-8">
<title>Praxisschild – Dr. Jonas Walbrecht</title>
<link rel="stylesheet" href="https://fonts.googleapis.com/css2?family=Raleway:wght@400;500;700;800&display=swap">
<style>
  :root {
    --practice-green: #03774a;
    --limeade: #d3d957;
    --sign-white: #ffffff;
  }
  * { margin: 0; padding: 0; box-sizing: border-box; }
  html, body {
    width: 1200px;
    height: 936px;
    overflow: hidden;
    background: var(--sign-white);
  }
  .sign {
    position: relative;
    width: 1200px;
    height: 936px;
    background: var(--sign-white);
    font-family: "Raleway", sans-serif;
    color: var(--practice-green);
  }
  .brand-mark {
    position: absolute;
    left: 81px;
    top: 95px;
    width: 192px;
    height: 192px;
  }
  .brand-divider {
    position: absolute;
    left: 337px;
    top: 95px;
    width: 2px;
    height: 194px;
    background: var(--practice-green);
  }
  .practice-name {
    position: absolute;
    left: 376px;
    top: 134px;
    font-size: 76px;
    font-weight: 800;
    line-height: 1;
    letter-spacing: -0.01em;
    color: var(--limeade);
    white-space: nowrap;
  }
  .practice-tagline {
    position: absolute;
    left: 378px;
    top: 222px;
    font-size: 31px;
    font-weight: 500;
    line-height: 1;
    letter-spacing: 0.26em;
    color: var(--practice-green);
    white-space: nowrap;
  }
  .qualifications {
    position: absolute;
    left: 378px;
    top: 356px;
    font-size: 44px;
    font-weight: 700;
    line-height: 61px;
    white-space: nowrap;
  }
  .hours {
    position: absolute;
    left: 378px;
    top: 486px;
    font-size: 35px;
    font-weight: 400;
    line-height: 46px;
    white-space: nowrap;
  }
  .hours-title {
    font-size: 33px;
    font-weight: 700;
    line-height: 40px;
    margin-bottom: 4px;
  }
  .hours-row {
    display: flex;
  }
  .hours-days { width: 233px; }
  .contact {
    position: absolute;
    left: 378px;
    top: 712px;
    font-size: 35px;
    font-weight: 400;
    line-height: 47px;
    white-space: nowrap;
  }
</style>
</head>
<body>
  <main class="sign">
    <svg class="brand-mark" viewBox="0 0 192 192" aria-hidden="true">
      <circle cx="96" cy="96" r="96" fill="var(--limeade)"/>
    </svg>
    <div class="brand-divider"></div>
    <h1 class="practice-name">Dr. Jonas Walbrecht</h1>
    <p class="practice-tagline">IHR HAUSARZT IN BEISPIELAU</p>

    <section class="qualifications">
      <p>Facharzt für Innere Medizin</p>
      <p>Facharzt für Allgemeinmedizin</p>
    </section>

    <section class="hours">
      <h2 class="hours-title">Sprechzeiten:</h2>
      <p class="hours-row"><span class="hours-days">Mo. - Fr.</span><span>7:30 – 12:00 Uhr</span></p>
      <p class="hours-row"><span class="hours-days">Die. - Do.</span><span>17:00 – 19:00 Uhr</span></p>
      <p>und nach Vereinbarung</p>
    </section>

    <section class="contact">
      <p>Tel: 0761 83172</p>
      <p>www.hausarzt-beispielau.de</p>
    </section>
  </main>
</body>
</html>
```